Mar-wick Sky Harbor Custom Brokers Limited

The Company deals with:
shipping
logistic
imports
Export
customs clearance (customs broker services); and
customers can shop online and we take care of the shipment from the United States of America to Jamaica.
(we offer freight forwarding services from USA to Kingston Jamaica
Our tagline is : Creating Waves in the Logistic Industry.
Address: Shop 9 Birchfield Trade Centre, 227-229 Welland Avenue Kingston 8, Jamaica West Indies Telephone: (876)555-0193
Example of what we required can be seem: www.swiftparcelhubexample.com

```html
<!DOCTYPE html>
<html lang="en">
<head>
<meta charset="utf-8">
<title>Mar-wick Sky Harbor Custom Brokers Limited</title>
<link href="https://fonts.googleapis.com/css2?family=Poppins:ital,wght@0,400;0,500;0,600;0,700;1,400&display=swap" rel="stylesheet">
<style>
:root{
  --gold:#eeaa00;
  --gold-deep:#c99000;
  --navy:#0f2c52;
  --ink:#1d3557;
  --text:#3d5a80;
  --muted:#8a94a3;
  --soft:#f7f7f7;
  --footer:#0d1b2e;
  --white:#fff;
}
*{margin:0;padding:0;box-sizing:border-box}
html,body{width:1200px;height:4152px;overflow:hidden}
body{font-family:'Poppins',sans-serif;color:var(--ink);background:var(--white);position:relative}
.abs{position:absolute}
a{color:inherit;text-decoration:none}

/* header */
.site-header{position:absolute;left:0;top:0;width:1200px;height:63px;background:var(--white);z-index:5}
.brand{position:absolute;left:70px;top:10px;display:flex;align-items:center;gap:8px}
.brand-mark{width:14px;height:14px;border-radius:50%;background:var(--gold)}
.brand-name{font-size:11px;font-weight:700;color:var(--navy);line-height:1.1;width:110px}
.main-nav{position:absolute;top:24px;left:454px;display:flex;gap:0}
.main-nav a{font-size:12px;font-weight:500;color:var(--navy);text-transform:uppercase;margin-right:37px}
.main-nav a.active{color:var(--gold);border-bottom:2px solid var(--gold);padding-bottom:3px}
.btn-signup{position:absolute;left:1007px;top:13px;width:121px;height:37px;border-radius:19px;background:var(--gold);color:#fff;font-weight:600;font-size:14px;display:flex;align-items:center;justify-content:center}

/* hero */
.hero{position:absolute;left:0;top:63px;width:1200px;height:620px}
.hero-photo{position:absolute;inset:0;background:linear-gradient(160deg,#3b3f5c 0%,#b5653a 30%,#e08a35 50%,#8a4a35 70%,#2a2f48 100%)}
.hero-wave{position:absolute;left:0;top:0}
.hero-title{position:absolute;left:229px;top:255px;font-size:41px;font-weight:700;color:#fff;line-height:53px}
.hero-text{position:absolute;left:229px;top:430px;font-size:12px;color:#fff;line-height:26px}
.btn-gold{position:absolute;background:var(--gold);color:#fff;border-radius:22px;font-size:13px;font-weight:500;display:flex;align-items:center;justify-content:center}

/* about */
.about-label{position:absolute;left:0;width:1200px;top:784px;text-align:center;font-size:14px;font-weight:500;color:var(--navy)}
.about-brand{position:absolute;left:0;width:1200px;top:826px;display:flex;justify-content:center;align-items:center;gap:8px}
.about-brand .brand-name{width:auto;font-size:12px}
.about-text{position:absolute;left:200px;width:800px;top:908px;text-align:center;font-size:13.5px;line-height:26px;color:var(--text)}
.features{position:absolute;left:142px;top:1035px;width:916px;display:flex}
.feature{width:229px;text-align:center;border-right:1px solid #dfe3ea;padding:0 16px;height:180px}
.feature:last-child{border-right:none}
.feature svg{width:52px;height:50px;stroke:var(--navy);fill:none;stroke-width:2}
.feature h3{font-size:16px;font-weight:500;color:var(--navy);margin-top:18px}
.feature p{font-size:12px;line-height:18.5px;color:var(--text);margin-top:10px}

/* services */
.services{position:absolute;left:0;top:1302px;width:1200px;height:510px;background:var(--soft)}
.section-title{position:absolute;left:0;width:1200px;text-align:center;font-weight:600;color:var(--navy)}
.title-rule{position:absolute;left:556px;width:88px;height:3px;background:var(--gold)}
.services-text{position:absolute;left:0;width:1200px;top:1436px;text-align:center;font-size:12px;line-height:23px;color:var(--muted)}
.tab{position:absolute;top:1538px;height:41px;border-radius:21px;border:2px solid #c8ccd2;color:var(--muted);font-size:14px;font-weight:500;display:flex;align-items:center;justify-content:center;background:var(--soft)}
.tab.active{border-color:var(--gold);color:var(--gold)}
.estimate-title{position:absolute;left:0;width:1200px;top:1609px;text-align:center;font-size:19px;font-weight:600;color:var(--navy)}
.field{position:absolute;top:1650px;height:61px;border:1px solid #d8dbe0;border-radius:4px;background:#fff;font-size:16px;display:flex;align-items:center;padding-left:14px}
.field.filled{color:var(--navy)}
.field.empty{color:#a3a9b3}
.field-label{position:absolute;top:1717px;font-size:12px;font-style:italic;color:var(--muted)}
.btn-check{position:absolute;left:839px;top:1650px;width:137px;height:61px;border-radius:5px;background:var(--gold);color:#fff;font-weight:600;font-size:15px;display:flex;align-items:center;justify-content:center}

/* different */
.diff-sub{position:absolute;left:0;width:1200px;top:1972px;text-align:center;font-size:14px;color:var(--text)}
.diff-wave{position:absolute;left:0;top:2390px}
.card{position:absolute;top:2048px;width:284px;height:417px;background:#fff;border-radius:6px;box-shadow:0 6px 22px rgba(15,44,82,.08);overflow:hidden}
.card-photo{height:188px}
.card h3{margin:40px 0 0 29px;font-size:16px;font-weight:600;color:var(--navy)}
.card p{margin:13px 28px 0 29px;font-size:12px;line-height:21px;color:var(--text)}
.card .dash{margin:19px 0 0 29px;width:34px;height:2px;background:var(--gold)}

/* split blocks */
.customs-band{position:absolute;left:0;top:2708px;width:741px;height:430px;background:var(--gold-deep)}
.import-band{position:absolute;left:457px;top:3138px;width:743px;height:430px;background:var(--navy)}
.photo{position:absolute}
.block-title{position:absolute;font-size:20px;font-weight:600;color:#fff}
.block-text{position:absolute;font-size:12px;line-height:23px;color:#fff;width:350px}
.btn-outline{position:absolute;height:44px;width:151px;border:1.5px solid #fff;border-radius:22px;color:#fff;font-size:13px;font-weight:500;display:flex;align-items:center;justify-content:center}

/* stores */
.recommended{position:absolute;left:0;width:1200px;top:3648px;text-align:center;font-size:13px;color:var(--gold)}
.store{position:absolute;top:3755px;width:208px;height:129px;border:1.5px solid #dde1e6;display:flex;align-items:center;justify-content:center;gap:8px;font-size:20px;font-weight:600;color:var(--navy)}
.store.featured{border:2px solid var(--gold)}
.store .dot{width:12px;height:12px;background:var(--gold)}

/* footer */
.site-footer{position:absolute;left:0;top:3963px;width:1200px;height:189px;background:var(--footer);color:#fff}
.footer-brand{position:absolute;left:151px;top:40px;display:flex;align-items:center;gap:10px}
.footer-brand .brand-name{color:#fff;font-size:18px;width:200px;line-height:1.25}
.footer-brand .sub{display:block;font-size:11px;font-weight:400;letter-spacing:3px;margin-top:4px}
.footer-nav{position:absolute;top:48px;left:564px;display:flex}
.footer-nav a{font-size:12px;font-weight:500;text-transform:uppercase;margin-right:36px}
.footer-nav a:last-child{margin-right:0}
.follow{position:absolute;right:153px;top:86px;display:flex;align-items:center;gap:8px;font-size:11px}
.follow strong{font-weight:600;margin-right:4px}
.social{display:flex;align-items:center;gap:4px}
.social i{width:14px;height:14px;border-radius:50%;background:var(--gold);display:inline-block}
.copyright{position:absolute;right:153px;top:146px;font-size:11px}
</style>
</head>
<body>

<header class="site-header">
  <div class="brand"><span class="brand-mark"></span><span class="brand-name">MAR-WICK SKY HARBOR</span></div>
  <nav class="main-nav">
    <a class="active">Home</a><a>About Us</a><a>Services</a><a>Shipping Calculator</a><a>Contact</a>
  </nav>
  <a class="btn-signup">Sign Up</a>
</header>

<section class="hero">
  <div class="hero-photo" role="img" aria-label="Sunset harbour with container terminal, cranes and a loaded cargo ship"></div>
  <svg class="hero-wave" width="1200" height="620" viewBox="0 0 1200 620">
    <path d="M0,410 C120,560 330,625 560,612 C800,598 1050,560 1200,610 L1200,620 L0,620 Z" fill="#fff"/>
    <path d="M0,410 C120,560 330,625 560,612 C800,598 1050,560 1200,610" fill="none" stroke="#eeaa00" stroke-width="5"/>
    <path d="M0,480 C120,600 330,640 560,625 C800,610 1050,580 1200,615 L1200,620 L0,620 Z" fill="#fff"/>
  </svg>
  <h1 class="hero-title">Creating Waves<br>In The Logistic<br>Industry.</h1>
  <p class="hero-text">Lorem Ipsum Dolor Sit Amet, Consetetur Sadipscing Elitr,<br>Sed Diam Nonumy Eirmod Tempor Invidunt Ut</p>
</section>
<a class="btn-gold" style="left:229px;top:570px;width:150px;height:44px">Learn More</a>

<section class="about">
  <p class="about-label">About Us</p>
  <div class="about-brand"><span class="brand-mark"></span><span class="brand-name">MAR-WICK SKY HARBOR</span></div>
  <p class="about-text">Lorem Ipsum Dolor Sit Amet, Consetetur Sadipscing Elitr, Sed Diam Nonumy Eirmod Tempor Invidunt Ut Labore Et Dolore Magna Aliquyam Erat, Sed Diam Voluptua. At Vero Eos Et Accusam Et Justo Duo Dolores Et Ea Rebum. Stet Clita Kasd Gubergren, No Sea Takimata Sanctus Est</p>
  <div class="features">
    <div class="feature">
      <svg viewBox="0 0 52 50"><path d="M6 14 L26 5 L46 14 L46 36 L26 45 L6 36 Z"/><path d="M6 14 L26 23 L46 14 M26 23 L26 45"/></svg>
      <h3>Storage</h3>
      <p>Lorem Ipsum Dolor Sit Amet, Consetetur Sadipscing Elitr, Sed Diam Nonumy Eirmod Tempor</p>
    </div>
    <div class="feature">
      <svg viewBox="0 0 52 50"><path d="M8 14 H32 V34 H8 Z M32 20 H42 L48 28 V34 H32"/><circle cx="16" cy="37" r="4"/><circle cx="40" cy="37" r="4"/></svg>
      <h3>Cargo</h3>
      <p>Lorem Ipsum Dolor Sit Amet, Consetetur Sadipscing Elitr, Sed Diam Nonumy Eirmod Tempor</p>
    </div>
    <div class="feature">
      <svg viewBox="0 0 52 50"><path d="M4 30 H48 L42 40 H10 Z M14 30 V20 H38 V30 M20 20 V12 H30 V20"/><path d="M2 45 Q8 42 14 45 T26 45 T38 45 T50 45"/></svg>
      <h3>Sea Freight</h3>
      <p>Lorem Ipsum Dolor Sit Amet, Consetetur Sadipscing Elitr, Sed Diam Nonumy Eirmod Tempor</p>
    </div>
    <div class="feature">
      <svg viewBox="0 0 52 50"><circle cx="26" cy="26" r="18"/><path d="M8 26 H44 M26 8 Q16 26 26 44 M26 8 Q36 26 26 44"/></svg>
      <h3>Worldwide Transport</h3>
      <p>Lorem Ipsum Dolor Sit Amet, Consetetur Sadipscing Elitr, Sed Diam Nonumy Eirmod Tempor</p>
    </div>
  </div>
</section>

<section class="services"></section>
<h2 class="section-title" style="top:1360px;font-size:38px">Our Service</h2>
<div class="title-rule" style="top:1414px"></div>
<p class="services-text">Lorem Ipsum Dolor Sit Amet, Consetetur Sadipscing Elitr, Sed Diam<br>Nonumy Eirmod Tempor Invidunt Ut Labore Et Dolore Magna Aliquyam</p>
<div class="tab active" style="left:313px;width:174px">SHIPPING RATES</div>
<div class="tab" style="left:516px;width:177px">TRACK SHIPPING</div>
<div class="tab" style="left:722px;width:164px">SERVICE POINT</div>
<h3 class="estimate-title">GET A FREE ESTIMATE</h3>
<div class="field filled" style="left:222px;width:237px">California</div>
<div class="field empty" style="left:477px;width:237px">Destination</div>
<div class="field empty" style="left:731px;width:91px">Weigh</div>
<a class="btn-check">CHECK NOW</a>
<span class="field-label" style="left:222px">Origin Shipment</span>
<span class="field-label" style="left:477px">Destination Shipment</span>
<span class="field-label" style="left:731px">Weight(Kg)</span>

<svg class="diff-wave" width="1200" height="228" viewBox="0 0 1200 228">
  <path d="M0,60 C200,0 400,100 650,60 C850,30 1000,20 1200,50 L1200,228 L0,228 Z" fill="#eef2f8"/>
  <path d="M0,110 C250,60 500,140 750,100 C950,70 1100,90 1200,80 L1200,228 L0,228 Z" fill="#e6ecf5"/>
</svg>
<h2 class="section-title" style="top:1900px;font-size:39px">What Make Us Different</h2>
<div class="title-rule" style="top:1952px"></div>
<p class="diff-sub">What we provide for clients</p>

<article class="card" style="left:151px">
  <div class="card-photo" role="img" aria-label="Two shop workers checking clothing items on a rack" style="background:linear-gradient(135deg,#c9b8a6,#6d7f96)"></div>
  <h3>IT STORE PICKUP</h3>
  <p>Lorem Ipsum Dolor Sit Amet, Consetetur Sadipscing Elitr, Sed Diam Nonumy Eirmod Tempor Invidunt Ut Labore Et Dolore</p>
  <div class="dash"></div>
</article>
<article class="card" style="left:457px">
  <div class="card-photo" role="img" aria-label="Two warehouse staff reviewing orders on a laptop among shelves" style="background:linear-gradient(135deg,#b9c3cf,#8a7a66)"></div>
  <h3>IT STORE PURCHASING</h3>
  <p>Lorem Ipsum Dolor Sit Amet, Consetetur Sadipscing Elitr, Sed Diam Nonumy Eirmod Tempor Invidunt Ut Labore Et Dolore</p>
  <div class="dash"></div>
</article>
<article class="card" style="left:764px">
  <div class="card-photo" role="img" aria-label="Delivery driver at the wheel of a van" style="background:linear-gradient(135deg,#d7dde4,#6c8aa8)"></div>
  <h3>BUSINESS DELIVERY</h3>
  <p>Lorem Ipsum Dolor Sit Amet, Consetetur Sadipscing Elitr, Sed Diam Nonumy Eirmod Tempor Invidunt Ut Labore Et Dolore</p>
  <div class="dash"></div>
</article>

<section class="customs-band"></section>
<div class="photo" role="img" aria-label="Warehouse workers in hard hats carrying boxes between tall shelves" style="left:599px;top:2781px;width:448px;height:357px;background:linear-gradient(135deg,#8d7a62,#3e5f7e)"></div>
<h3 class="block-title" style="left:205px;top:2832px">CUSTOMS CLEARANCE</h3>
<p class="block-text" style="left:205px;top:2882px">Lorem Ipsum Dolor Sit Amet, Consetetur Sadipscing Elitr, Sed Diam Nonumy Eirmod Tempor Invidunt Ut Labore Et Dolore Magna Aliquyam Erat, Sed Diam Voluptua. At Vero Eos Et Accusam Et Justo Duo Dolores Et Ea Rebum. Stet Clita Kasd Gubergren, No Sea Takimata Sanctus Est</p>
<a class="btn-outline" style="left:205px;top:3043px">Learn More</a>

<section class="import-band"></section>
<div class="photo" role="img" aria-label="Aerial view of a container port with cranes at dusk" style="left:151px;top:3138px;width:448px;height:358px;background:linear-gradient(135deg,#6f7d96,#c27a45 55%,#3a4660)"></div>
<h3 class="block-title" style="left:672px;top:3185px">IMPORT AND EXPORTATION</h3>
<p class="block-text" style="left:672px;top:3240px">Lorem Ipsum Dolor Sit Amet, Consetetur Sadipscing Elitr, Sed Diam Nonumy Eirmod Tempor Invidunt Ut Labore Et Dolore Magna Aliquyam Erat, Sed Diam Voluptua. At Vero Eos Et Accusam Et Justo Duo Dolores Et Ea Rebum. Stet Clita Kasd Gubergren, No Sea Takimata Sanctus Est</p>
<a class="btn-outline" style="left:672px;top:3407px">Learn More</a>

<p class="recommended">recommended</p>
<h2 class="section-title" style="top:3672px;font-size:39px">Online Stores</h2>
<div class="store featured" style="left:151px"><span class="dot"></span>Shopnova</div>
<div class="store" style="left:382px"><span class="dot"></span>Volt Mart</div>
<div class="store" style="left:611px"><span class="dot"></span>Lotstand</div>
<div class="store" style="left:839px"><span class="dot"></span>Pantry Row</div>

<footer class="site-footer">
  <div class="footer-brand"><span class="brand-mark"></span><span class="brand-name">MAR-WICK SKY HARBOR<span class="sub">Custom Brokers Ltd.</span></span></div>
  <nav class="footer-nav"><a>Home</a><a>About Us</a><a>Services</a><a>Shipping Calculator</a><a>Contact</a></nav>
  <div class="follow"><strong>Follow Us:</strong>
    <span class="social"><i></i>Friendsy</span>
    <span class="social"><i></i>Chirper</span>
    <span class="social"><i></i>Viewtube</span>
  </div>
  <p class="copyright">Copyright © 2020 Mar-wick-Sky-Harbor.</p>
</footer>

</body>
</html>
```